Business card design needed

A laid back coffee shop that has a great feel, that becomes a bar and grill at night. We are also wanting to cater for functions etc.
The business itself is painted dark blue/charcoal and has red doors.
Would like a logo that will be recognised when seen.

Industry/Entity Type

Coffee Shop

Contact Information for Business Card

The Lantern Coffee Bar & Grill
14b Wattlebrook St
Kelmarra NSW 2318
Ph. 02 4817 6293

Logo Text

Logo styles of interest
Emblem Logo
Abstract Logo
Wordmark Logo
Requirements
Must have
• A loyalty card on the back with 2 rows of 7 stamp spaces and a place to write a name and phone number (for a draw)

```html
<!DOCTYPE html>
<html lang="en">
<head>
<meta charset="utf-8">
<title>The Lantern Coffee Bar &amp; Grill – Business Card</title>
<link rel="stylesheet" href="https://fonts.googleapis.com/css2?family=Poiret+One&display=swap">
<style>
  :root {
    --page: #ffffff;
    --card: #ffffff;
    --ink: #3a3a3a;
    --ink-soft: #8a8a8a;
    --rule: #444444;
    --brand-red: #e0110f;
    --warm-orange: rgba(235, 154, 42, 0.32);
    --warm-yellow: rgba(246, 209, 90, 0.18);
    --stamp: #c9c9c9;
    --stamp-fill: rgba(240, 240, 240, 0.8);
    --stamp-gold: #b58a3c;
    --stamp-gold-fill: rgba(200, 170, 110, 0.3);
    --highlight: rgba(210, 210, 210, 0.6);
    --shadow: rgba(90, 100, 100, 0.55);
  }
  html, body { margin: 0; padding: 0; overflow: hidden; }
  body {
    width: 1200px; height: 1000px; position: relative;
    background: var(--page);
    font-family: "Poiret One", sans-serif;
    color: var(--ink);
  }
  .card {
    position: absolute; left: 288px; width: 668px; height: 378px;
    background: var(--card); overflow: hidden;
    box-shadow: 6px 8px 10px var(--shadow);
  }
  .card--front { top: 62px; }
  .card--back { top: 510px; }
  .card__backdrop {
    position: absolute; inset: 0;
    background:
      radial-gradient(ellipse 60% 80% at 75% 40%, var(--warm-orange), transparent 70%),
      radial-gradient(ellipse 50% 70% at 30% 90%, var(--warm-yellow), transparent 70%);
  }

  /* front */
  .wordmark { position: absolute; left: 40px; top: 42px; width: 290px; text-align: center; color: var(--ink-soft); }
  .wordmark__circle { width: 110px; height: 110px; margin: 0 auto 40px; border: 5px solid var(--brand-red); border-radius: 50%; box-sizing: border-box; }
  .wordmark__name { font-size: 44px; line-height: 1; }
  .wordmark__tag { font-size: 21px; margin-top: 8px; }
  .divider { position: absolute; left: 331px; top: 88px; width: 3px; height: 202px; background: var(--rule); }
  .address { position: absolute; left: 370px; top: 132px; width: 220px; text-align: center; font-size: 17px; line-height: 29px; font-style: normal; }
  .address span { background: var(--highlight); padding: 0 2px; }

  /* back */
  .field-label { position: absolute; left: 64px; font-size: 19px; color: var(--ink-soft); line-height: 1; }
  .field-label--name { top: 58px; }
  .field-label--phone { top: 126px; }
  .field-line { position: absolute; border-bottom: 1.5px dashed var(--ink-soft); height: 0; }
  .field-line--name { left: 168px; top: 76px; width: 430px; }
  .field-line--phone { left: 272px; top: 140px; width: 326px; }
  .stamps { position: absolute; left: 26px; top: 166px; display: grid; grid-template-columns: repeat(7, 56px); gap: 12px 15px; }
  .stamp { width: 56px; height: 56px; border-radius: 50%; border: 5px solid var(--stamp); box-sizing: border-box; background: var(--stamp-fill); }
  .stamp--reward { border-color: var(--stamp-gold); background: var(--stamp-gold-fill); }
  .back-name { position: absolute; left: 32px; top: 316px; font-size: 23px; line-height: 1; color: var(--ink); }
  .back-mark { position: absolute; left: 522px; top: 186px; width: 120px; text-align: center; color: var(--ink-soft); }
  .back-mark__circle { width: 70px; height: 70px; margin: 0 auto 12px; border: 5px solid var(--brand-red); border-radius: 50%; box-sizing: border-box; }
  .back-mark__name { font-size: 20px; line-height: 1; }
</style>
</head>
<body>
  <section class="card card--front">
    <div class="card__backdrop" role="img" aria-label="Warm coffee ring stain artwork"></div>
    <div class="wordmark">
      <div class="wordmark__circle"></div>
      <div class="wordmark__name">The Lantern</div>
      <div class="wordmark__tag">Coffee Bar &amp; Grill</div>
    </div>
    <div class="divider"></div>
    <address class="address">
      <span>14b Wattlebrook St</span><br>
      <span>Kelmarra</span><br>
      <span>NSW 2318</span><br>
      <span>Ph. 02 4817 6293</span>
    </address>
  </section>

  <section class="card card--back">
    <div class="card__backdrop" role="img" aria-label="Warm coffee ring stain artwork"></div>
    <div class="field-label field-label--name">Name</div>
    <div class="field-line field-line--name"></div>
    <div class="field-label field-label--phone">Phone Number</div>
    <div class="field-line field-line--phone"></div>
    <div class="stamps">
      <div class="stamp"></div><div class="stamp"></div><div class="stamp"></div><div class="stamp"></div><div class="stamp"></div><div class="stamp"></div><div class="stamp stamp--reward"></div>
      <div class="stamp"></div><div class="stamp"></div><div class="stamp"></div><div class="stamp"></div><div class="stamp"></div><div class="stamp"></div><div class="stamp stamp--reward"></div>
    </div>
    <div class="back-name">The Lantern Coffee Bar &amp; Grill</div>
    <div class="back-mark">
      <div class="back-mark__circle"></div>
      <div class="back-mark__name">The Lantern</div>
    </div>
  </section>
</body>
</html>
```